TALM needs a beautiful/corp web page

We are a pump an compressor repair facility in Alberta Canada. We love clean looks. white yellows greens blues. main page should involve conola fields, sun shine

Reason: i will be guaranteeing the project keep up the good work

Requirements
Must have
• open conola fields

```html
<!DOCTYPE html>
<html lang="en">
<head>
<meta charset="utf-8">
<title>TALM – Get in touch</title>
<link rel="stylesheet" href="https://fonts.googleapis.com/css2?family=Noto+Sans:wght@400;700&family=Questrial&display=swap">
<style>
  :root {
    --page-bg: #ffffff;
    --text-body: #555555;
    --text-heading: #222222;
    --text-muted: #666666;
    --rule: #dddddd;
    --rule-dot: #d9d9d9;
    --panel-bg: #f4f3f1;
    --field-border: #9a9a9a;
    --placeholder: #8a8a8a;
    --accent-green: #9ccc1e;
    --accent-yellow: #f4b93a;
    --client-border: #dcdcdc;
    --client-grey: #8c8c8c;
    --client-red: #e0201c;
    --footer-bg: #262223;
    --footer-text: #a39f9f;
  }
  * { box-sizing: border-box; margin: 0; padding: 0; }
  html, body {
    width: 1200px; height: 972px; overflow: hidden;
    background: var(--page-bg);
  }
  body { position: relative; font-family: "Noto Sans", sans-serif; color: var(--text-body); }

  .intro {
    position: absolute; left: 111px; top: -6px; width: 986px;
    text-align: center; font-size: 15.5px; line-height: 18px;
  }
  .intro p + p { margin-top: 22px; }

  .section-title {
    position: absolute; left: 94px; width: 1012px; height: 20px;
    display: flex; align-items: center;
  }
  .section-title .rule { flex: 1; height: 2px; background: var(--rule); }
  .section-title .dot { width: 9px; height: 9px; border-radius: 50%; background: var(--rule-dot); }
  .section-title h2 {
    font-family: "Questrial", sans-serif; font-weight: 400;
    font-size: 23px; letter-spacing: 3px; color: var(--text-heading);
    padding: 0 26px 0 28px; white-space: nowrap;
  }
  .contact-title { top: 165px; }
  .clients-title { top: 623px; }
  .contact-title .rule:first-child { flex: 0 0 344px; }
  .clients-title .rule:first-child { flex: 0 0 396px; }

  .contact-card {
    position: absolute; left: 94px; top: 229px; width: 474px; height: 288px;
    background: var(--panel-bg); padding: 30px 0 0 77px; color: var(--text-muted);
  }
  .contact-card h3 { font-size: 27px; font-weight: 700; letter-spacing: -0.2px; }
  .contact-card address {
    font-style: normal; font-size: 21px; line-height: 33px; margin-top: 30px;
  }
  .contact-card .email { color: var(--accent-green); }

  .contact-form { position: absolute; left: 623px; top: 229px; width: 476px; }
  .field {
    display: block; width: 474px; height: 38px; margin-bottom: 17px;
    border: 1px solid var(--field-border); background: #fff;
    font-family: "Noto Sans", sans-serif; font-size: 15px; color: var(--placeholder);
    padding: 9px 21px; line-height: 18px;
  }
  .field.message { height: 122px; margin-bottom: 23px; }
  .submit {
    display: block; margin-left: 345px; width: 131px; height: 50px;
    background: var(--accent-yellow); color: #fff; border: none;
    font-family: "Noto Sans", sans-serif; font-size: 15px; font-weight: 700;
  }

  .client-strip {
    position: absolute; left: 95px; top: 686px; width: 1012px; height: 102px;
    border: 1px solid var(--client-border);
    display: flex; align-items: center; justify-content: space-around; padding: 0 18px;
  }
  .client {
    display: flex; align-items: center; gap: 8px;
    font-family: "Noto Sans", sans-serif; font-weight: 700; font-size: 22px;
    color: var(--client-grey);
  }
  .client .mark { width: 18px; height: 18px; background: currentColor; }
  .client .mark.round { border-radius: 50%; }
  .client.featured { color: var(--client-red); }

  .site-footer {
    position: absolute; left: 0; top: 850px; width: 1200px; height: 122px;
    background: var(--footer-bg); text-align: center;
    font-family: "Questrial", sans-serif; color: var(--footer-text);
  }
  .footer-nav { margin-top: 17px; font-size: 14.5px; letter-spacing: 1.3px; }
  .footer-info { margin-top: 6px; font-size: 13px; letter-spacing: 1.1px; }
  .sep { margin: 0 13px; }
</style>
</head>
<body>
  <section class="intro">
    <p>Sed ut perspiciatis unde omnis iste natus error sit voluptatem accusantium doloremque laudantium, totam rem aperiam, eaque ipsa quae<br>ab illo inventore veritatis et.</p>
    <p>Quasi arch sed ut perspiciatis unde omnis iste natus error sit voluptatem accusantim doloremque laudantium, totam rem aperiam, eaque<br>ipsa quae ab illo inventore veritatis et quasi arch.</p>
  </section>

  <div class="section-title contact-title">
    <span class="rule"></span><span class="dot"></span>
    <h2>Get in touch with us</h2>
    <span class="dot"></span><span class="rule"></span>
  </div>

  <aside class="contact-card">
    <h3>TALM Rotating Solutions</h3>
    <address>
      111 Address, City, State 0000<br>
      Phone number 000.000.000<br>
      <span class="email">mail@talm.com</span>
    </address>
  </aside>

  <form class="contact-form">
    <div class="field">Your name</div>
    <div class="field">E-mail Address</div>
    <div class="field">Subject</div>
    <div class="field message">Message</div>
    <button class="submit" type="button">SUBMIT</button>
  </form>

  <div class="section-title clients-title">
    <span class="rule"></span><span class="dot"></span>
    <h2>Our Clients</h2>
    <span class="dot"></span><span class="rule"></span>
  </div>

  <div class="client-strip">
    <span class="client featured"><span class="mark"></span>Korvel</span>
    <span class="client"><span class="mark round"></span>Birchway</span>
    <span class="client"><span class="mark round"></span>Northdale</span>
    <span class="client"><span class="mark"></span>Ironfield</span>
    <span class="client"><span class="mark"></span>Quarto</span>
  </div>

  <footer class="site-footer">
    <nav class="footer-nav">Home<span class="sep">I</span>Products<span class="sep">I</span>Solutions<span class="sep">I</span>Choose us<span class="sep">I</span>About us<span class="sep">I</span>Contact</nav>
    <div class="footer-info">Your info mail<span class="sep">I</span>Address<span class="sep">I</span>Phone number</div>
  </footer>
</body>
</html>
```